Business Card Design for Small Electrical Contractor

I need to update my business card into something a little more modern. We are a small electrical contracting company. We service domestic and commercial places around Sydney. We have 2 logo designs at the moment. I have uploaded both and 2 different sizes to work with.

Industry/Entity Type

Business

Contact Information for Business Card

Leo Hartigan
8/21-23 Birch Rd, Kelsworth 2087
t - (02) 9381 4720
m - 0427 815 903
E - info@hartiganelx.com.au
W - hartiganelx.com.au
ABN: 42 907 551 316

Font styles to use
Sans Serif

Requirements
Must have
• I would also like to see the below fit on somewhere aswell
• - Licensed Electrician
• - Level 2 (Cat 1 & 4)
• - Domestic
• - Commercial
• - Repairs and Installations
• - Data
Nice to have
• Try and keep similar colours as logo
Should not have
• No lightning bolts or light globes. Smart and professional please.

```html
<!DOCTYPE html>
<html lang="en">
<head>
<meta charset="utf-8">
<title>Hartigan Electrical – Business Card</title>
<link href="https://fonts.googleapis.com/css2?family=Questrial&display=swap" rel="stylesheet">
<style>
  :root {
    --bg: #eceeef;
    --card: #ffffff;
    --ink: #1d4543;
    --orange: #e8912d;
    --band-dark: #071615;
    --band-teal: #0f4442;
    --band-text: #e6ecec;
  }
  * { margin: 0; padding: 0; box-sizing: border-box; }
  html, body { width: 1200px; height: 1200px; overflow: hidden; }
  body {
    background: var(--bg);
    font-family: "Questrial", "Century Gothic", sans-serif;
    color: var(--ink);
    position: relative;
  }
  .card {
    position: absolute;
    left: 100px; top: 294px;
    width: 1000px; height: 611px;
    background: var(--card);
    box-shadow: 0 10px 30px rgba(0,0,0,0.12);
    overflow: hidden;
  }
  .card__band { position: absolute; inset: 0; }
  .holder-name {
    position: absolute; left: 60px; top: 52px;
    font-size: 34px; font-variant: small-caps; letter-spacing: 1px;
    color: var(--ink);
  }
  .holder-rule {
    position: absolute; left: 60px; top: 100px;
    width: 250px; height: 3px; background: var(--orange);
  }
  .company-name {
    position: absolute; right: 60px; top: 44px;
    font-size: 34px; color: var(--ink);
  }
  .company-rule {
    position: absolute; right: 60px; top: 92px;
    width: 330px; height: 3px; background: var(--orange);
  }
  .contacts { position: absolute; left: 60px; top: 168px; list-style: none; }
  .contacts li {
    display: flex; align-items: center; gap: 14px;
    font-size: 25px; line-height: 36px; color: var(--ink);
  }
  .contacts svg { width: 24px; height: 24px; flex: none; }
  .location {
    position: absolute; left: 640px; top: 116px;
    display: flex; gap: 14px;
  }
  .location svg { width: 24px; height: 30px; margin-top: 6px; flex: none; }
  .location p { font-size: 25px; line-height: 32px; color: var(--ink); }
  .services {
    position: absolute; left: 40px; top: 420px;
    font-size: 25px; line-height: 32px; color: var(--band-text);
  }
  .licence {
    position: absolute; right: 50px; top: 296px; text-align: right;
    font-size: 25px; line-height: 32px; color: var(--band-text);
  }
  .web {
    position: absolute; left: 390px; top: 540px;
    font-size: 27px; letter-spacing: 2px; color: var(--band-text);
  }
</style>
</head>
<body>
  <section class="card" aria-label="Hartigan Electrical business card">
    <svg class="card__band" viewBox="0 0 1000 611" aria-hidden="true">
      <defs>
        <radialGradient id="bandFill" cx="0.55" cy="0.75" r="0.7">
          <stop offset="0" stop-color="var(--band-teal)"/>
          <stop offset="1" stop-color="var(--band-dark)"/>
        </radialGradient>
      </defs>
      <polygon points="0,372 1000,238 1000,611 0,611" fill="var(--orange)"/>
      <polygon points="0,380 1000,246 1000,611 0,611" fill="url(#bandFill)"/>
    </svg>

    <div class="holder-name">Leo Hartigan</div>
    <div class="holder-rule"></div>

    <div class="company-name">Hartigan Electrical</div>
    <div class="company-rule"></div>

    <ul class="contacts">
      <li>
        <svg viewBox="0 0 24 24"><path d="M6.6 10.8a15 15 0 0 0 6.6 6.6l2.2-2.2a1 1 0 0 1 1-.25 11.4 11.4 0 0 0 3.6.57 1 1 0 0 1 1 1V20a1 1 0 0 1-1 1A17 17 0 0 1 3 4a1 1 0 0 1 1-1h3.5a1 1 0 0 1 1 1c0 1.25.2 2.45.57 3.57a1 1 0 0 1-.25 1z" fill="var(--orange)"/></svg>
        (02) 9381 4720
      </li>
      <li>
        <svg viewBox="0 0 24 24"><rect x="6" y="2" width="12" height="20" rx="2" fill="none" stroke="var(--orange)" stroke-width="2"/><circle cx="12" cy="18.5" r="1.2" fill="var(--orange)"/></svg>
        0427 815 903
      </li>
      <li>
        <svg viewBox="0 0 24 24"><rect x="2" y="5" width="20" height="14" rx="1.5" fill="var(--orange)"/><path d="M2.5 6 12 13l9.5-7" fill="none" stroke="#fff" stroke-width="1.6"/></svg>
        info@hartiganelx.com.au
      </li>
    </ul>

    <div class="location">
      <svg viewBox="0 0 24 30"><path d="M12 1a10 10 0 0 0-10 10c0 7.5 10 18 10 18s10-10.5 10-18A10 10 0 0 0 12 1z" fill="var(--orange)"/><circle cx="12" cy="11" r="4" fill="#fff"/></svg>
      <p>8/21-23 Birch Rd,<br>Kelsworth 2087<br>ABN 42 907 551 316</p>
    </div>

    <p class="services">Commercial<br>Installations and Repairs<br>Data</p>
    <p class="licence">Licensed Electrician<br>Level 2 (Cat 1 &amp; 4)<br>Domestic</p>
    <p class="web">www.hartiganelx.com.au</p>
  </section>
</body>
</html>
```